Business Card Design Project

We would like you to create business cards. The color scheme should match our website and logo. I have attached an image of a page of our website, as well as our logo. Please Please include the logo on the left with a similar faded horizontal line, and a blueprint type sketch of a house on cribbing on the right, similar to our website. We like the idea of how this looks. I have attached a third image of an actual house on cribbing (crisscrossed wooden beams). Please include cribbing in the blueprint type sketch.

The information to be included on the business cards is

(name)
214 Fernbrook Avenue
Suite 317
West Orange, NJ 07148
732.418.2093
www.keystonebeamworksofnj.example
info@keystonebeamworksofnj.example

This information can be spaced in any way.

I will also be posting a job for letterhead using the same design as the business cards.

If you need anything other information or I have not been clear enough, please do not hesitate to message me.

Thank you!
Updates

This design project is now open to all designers.  Please message me with any questions.  Thank you.

Industry/Entity Type

House

Requirements
Must have
• 1. Our logo
2. Blueprint type sketch of a house on wooden cribbing.
3. Color scheme to match logo and website.
4. Information provided.

```html
<!DOCTYPE html>
<html lang="en">
<head>
<meta charset="utf-8">
<title>Keystone Beamworks of NJ — Business Card</title>
<link href="https://fonts.googleapis.com/css2?family=Source+Sans+3:wght@400;600&display=swap" rel="stylesheet">
<style>
  :root {
    --backdrop: #b3c3c8;
    --band-cyan: #00e2ff;
    --band-mid: #0a8cff;
    --band-blue: #0033ff;
    --paper: #ffffff;
    --sketch-pale: #eaf8fd;
    --sketch-mid: #cdeef9;
    --sketch-blue: #a9def2;
    --name-ink: #2a2e33;
    --accent-orange: #f7941d;
    --contact-blue: #3ec7f6;
  }
  * { margin: 0; padding: 0; box-sizing: border-box; }
  html, body {
    width: 1200px;
    height: 753px;
    overflow: hidden;
    background: var(--backdrop);
  }
  .card {
    position: absolute;
    left: 71px;
    top: 72px;
    width: 1039px;
    height: 598px;
    background: var(--paper);
    font-family: "Source Sans 3", "Myriad Pro", sans-serif;
  }
  .band {
    position: absolute;
    left: 0;
    width: 100%;
    background: linear-gradient(90deg, var(--band-cyan) 0%, var(--band-mid) 50%, var(--band-blue) 100%);
  }
  .band--top { top: 0; height: 203px; }
  .band--bottom { bottom: 0; height: 115px; }
  .header-panel {
    position: absolute;
    left: 60px;
    top: 59px;
    width: 921px;
    height: 144px;
    background: var(--paper);
    border-radius: 10px 10px 0 0;
    overflow: hidden;
  }
  .blueprint-sketch {
    position: absolute;
    right: 0;
    top: 0;
    width: 562px;
    height: 100%;
    background: linear-gradient(90deg, var(--paper) 0%, var(--sketch-pale) 22%, var(--sketch-mid) 60%, var(--sketch-blue) 100%);
  }
  .brand {
    position: absolute;
    left: 70px;
    top: 222px;
    display: flex;
    align-items: flex-start;
    gap: 12px;
  }
  .brand__mark {
    flex: none;
    width: 22px;
    height: 22px;
    margin-top: 12px;
    background: var(--accent-orange);
  }
  .brand__name {
    font-size: 40px;
    font-weight: 600;
    color: var(--name-ink);
    line-height: 48px;
  }
  .tagline {
    position: absolute;
    left: 92px;
    top: 340px;
    font-size: 17px;
    line-height: 22px;
    color: var(--accent-orange);
    display: flex;
    align-items: center;
    gap: 8px;
  }
  .tagline__dot {
    width: 10px;
    height: 10px;
    border-radius: 50%;
    background: var(--accent-orange);
  }
  .contact {
    position: absolute;
    left: 579px;
    top: 267px;
    list-style: none;
    font-size: 26px;
    line-height: 29px;
    color: var(--contact-blue);
  }
</style>
</head>
<body>
  <div class="card">
    <div class="band band--top"></div>
    <div class="band band--bottom"></div>

    <div class="header-panel">
      <div class="blueprint-sketch" role="img" aria-label="Faded blueprint-style line sketch of a house raised on crisscrossed wooden cribbing"></div>
    </div>

    <div class="brand">
      <span class="brand__mark"></span>
      <span class="brand__name">Keystone Beamworks<br>of NJ</span>
    </div>

    <p class="tagline">
      <span class="tagline__dot"></span>
      House Raising Construction Masonry
      <span class="tagline__dot"></span>
    </p>

    <ul class="contact">
      <li>214 Fernbrook Avenue</li>
      <li>Suite 317</li>
      <li>West Orange, NJ 07148</li>
      <li>732.418.2093</li>
      <li>www.keystonebeamworksofnj.example</li>
      <li>info@keystonebeamworksofnj.example</li>
    </ul>
  </div>
</body>
</html>
```